Tarvoe Aviation Consultants Business card

I need a business card design for a new aviation company called Tarvoe Aviation Consultants. Our focus is on large airplane end-of-life solutions. This is typically where an airline retires an aircraft and we would oversee the dismantling of the aircraft into the valuable components and parts. The removed parts are then overhauled and reintroduced into the market place.
'Tarvoe' means 'island in the clouds'. I envision an airplane flying into the sunset as it's days are numbered. I am also very keen on our Florida island vibe.
Industry/Entity Type
Aviation
Contact Information for Business Card
Tarvoe Aviation Consultants
End of Life Specialists
Glen Morsk - President
418 SW 27th Ave
Fort Lauderdale, FL 33872
+1 954 555-0183
Logo Text
Requirements
Must have
- airplane
Nice to have
- sunset
- somewhere on the card it would be the definition of 'Tarvoe' - island in the clouds

```html
<!DOCTYPE html>
<html lang="en">
<head>
<meta charset="utf-8">
<title>Tarvoe Aviation Consultants – Business Card</title>
<link rel="stylesheet" href="https://fonts.googleapis.com/css2?family=Oswald:wght@500&family=Lato:wght@400;700&display=swap">
<style>
  :root {
    --ocean-blue: #0b7aa6;
    --sunset-orange: #efa716;
    --card-white: #ffffff;
    --card-shade: #eeeeef;
    --tagline-grey: #8a8c90;
    --page-bg: #e6e8eb;
  }
  html, body {
    margin: 0;
    width: 1200px;
    height: 900px;
    overflow: hidden;
    background: var(--page-bg);
  }
  .card {
    position: absolute;
    left: 120px;
    top: 152px;
    width: 960px;
    height: 595px;
    background: linear-gradient(180deg, var(--card-white) 0%, var(--card-shade) 100%);
    box-shadow: 0 10px 30px rgba(0,0,0,0.15);
    overflow: hidden;
    font-family: "Lato", sans-serif;
  }
  .card-shapes {
    position: absolute;
    inset: 0;
  }
  .brand-mark {
    position: absolute;
    left: 53px;
    top: 59px;
    width: 108px;
    height: 108px;
    border: 3px solid var(--ocean-blue);
    border-radius: 50%;
    box-sizing: border-box;
  }
  .brand-name {
    position: absolute;
    left: 197px;
    top: 88px;
    margin: 0;
    font-family: "Oswald", sans-serif;
    font-weight: 500;
    font-size: 37px;
    line-height: 48px;
    letter-spacing: 0.01em;
    color: var(--ocean-blue);
    text-transform: uppercase;
  }
  .brand-tagline {
    position: absolute;
    left: 199px;
    top: 136px;
    margin: 0;
    font-size: 14px;
    letter-spacing: 0.62em;
    color: var(--tagline-grey);
    text-transform: uppercase;
  }
  .plane-art {
    position: absolute;
    left: 631px;
    top: 191px;
    width: 273px;
    height: 74px;
    border-radius: 37px 10px 37px 10px;
    background: linear-gradient(90deg, #f5b73a 0%, var(--sunset-orange) 100%);
  }
  .contact-list {
    position: absolute;
    right: 52px;
    top: 344px;
    margin: 0;
    padding: 0;
    list-style: none;
    color: var(--card-white);
    font-size: 25px;
    line-height: 34.5px;
    text-align: right;
  }
  .contact-list li {
    display: flex;
    justify-content: flex-end;
    align-items: center;
    gap: 10px;
  }
  .contact-icon {
    width: 22px;
    height: 22px;
    flex: none;
  }
  .person {
    position: absolute;
    left: 64px;
    top: 476px;
  }
  .person-name {
    margin: 0;
    font-size: 36px;
    line-height: 42px;
    color: var(--sunset-orange);
    text-transform: uppercase;
  }
  .person-title {
    margin: 0;
    font-size: 25px;
    line-height: 34px;
    color: var(--card-white);
  }
  .address {
    position: absolute;
    right: 52px;
    top: 482px;
    margin: 0;
    font-style: normal;
    font-size: 25px;
    line-height: 35px;
    color: var(--card-white);
    text-align: right;
  }
</style>
</head>
<body>
  <section class="card" aria-label="Tarvoe Aviation Consultants business card">
    <svg class="card-shapes" width="960" height="595" viewBox="0 0 960 595" aria-hidden="true">
      <polygon class="flight-trail" points="0,425 654,262 0,441" fill="var(--ocean-blue)"/>
      <polygon class="ocean-band" points="0,451 960,206 960,595 0,595" fill="var(--ocean-blue)"/>
    </svg>

    <div class="brand-mark" aria-hidden="true"></div>
    <h1 class="brand-name">Tarvoe Aviation Consultants</h1>
    <p class="brand-tagline">End of Life Specialists</p>

    <div class="plane-art" role="img" aria-label="Orange airplane silhouette climbing away along the trail"></div>

    <ul class="contact-list">
      <li>+1 954 555-0183
        <svg class="contact-icon" viewBox="0 0 24 24" aria-hidden="true"><path d="M6.6 2.5l3 3.4-1.8 2.6c1.2 2.6 3.2 4.6 5.7 5.8l2.6-1.8 3.4 3-1.6 3.4C11 18.6 5.4 13 4.2 4.1z" fill="var(--sunset-orange)"/></svg>
      </li>
      <li>info@tarvoeaviation.com
        <svg class="contact-icon" viewBox="0 0 24 24" aria-hidden="true"><rect x="3" y="6" width="18" height="13" fill="var(--sunset-orange)"/><path d="M3 6l9 7 9-7" fill="none" stroke="var(--ocean-blue)" stroke-width="1.6"/></svg>
      </li>
      <li>www.tarvoeaviation.com
        <svg class="contact-icon" viewBox="0 0 24 24" aria-hidden="true"><circle cx="12" cy="12" r="9.5" fill="var(--sunset-orange)"/><path d="M7 9c2-1 3 1 5 0s2 3 0 4-1 4-3 3-1-3-2-4 0-2 0-3z" fill="var(--ocean-blue)"/></svg>
      </li>
    </ul>

    <div class="person">
      <p class="person-name">Glen Morsk</p>
      <p class="person-title">President</p>
    </div>

    <address class="address">418 SW 27th Ave<br>Fort Lauderdale, FL 33872</address>
  </section>
</body>
</html>
```